依頼概要
■依頼の目的
マタニティさん向けの本の表紙デザインをお願いします。

■本の内容
胎内記憶による、しあわせな出産と育児のためのマタニティライフの過ごし方

第一章 胎内記憶を知ってマタニティライフを過ごしましょう
第二章 おなかの赤ちゃんとコミュニケーション
第三章 しあわせなお産をしよう
第四章 出産後のことを考えておこう
第五章 0歳育児が大切なことは意外と知られていない
第六章 夫婦で妊娠出産を楽しむ~産後うつを防ぐ~

差し支えなければですが、「0歳児についてわかるサブキャッチ」を表紙にデザインしたいのでよろしくお願いします。

■デザイン要望
柔らかい雰囲気の若いママ向けのおしゃれな感じが望ましいです。

■著者の記載

全国育み言葉研究会認定講師
マタニティライフしあわせアドバイザー
北浦ミレーユ詩織

※どこかに
「胎内記憶の世界的第一人者
森下晃先生 推薦」を入れてほしいです。

その他 ご不明な点がございましたらお気軽にご質問下さい。
よろしくお願いいたします。
書き損じておりました。
電子書籍(Pagora)での出版になります。

画像サイズは
表紙ファイルの理想的な寸法は2560×1600ピクセルです。
画像の寸法は1000×625ピクセル以上であることが必要です。

次点、次次点のかたへの参加報酬を設定いたしました。
皆様の自由な発想のデザインを楽しみにしております。

その他、必要な情報がありましたらお問い合わせください。
ランサーのみなさま、たくさんおご提案ありがとうございました。
どれも秀逸で感動しております。
2月末までに決定させていただきたいと思います。
よろしくお願いいたします。
■ 選んだ理由

どれもかわいいデザインで迷いましたが、
美しい写真でクオリティが高いこと、一目でマタニティの本であるとわかること、
「お産が楽になる」という言葉を大きく書いてくださっているのを選ぶようにとアドバイスされました。

■ 提案者全員のお礼・コメント

自分ではとうてい思いつかないような、かわいくてわかりやすいデザインを考えてくださり、感動しました。原稿を読んで下さり、内容も考慮して下さって感謝の気持ちで一杯です。
本当に迷いました。今回はご縁がなかったかたも、すばらしいものばかりでした。ありがとうございました!!

```html
<!DOCTYPE html>
<html lang="ja">
<head>
<meta charset="UTF-8">
<title>お産が軽くなる 胎内記憶の物語</title>
<link rel="stylesheet" href="https://fonts.googleapis.com/css2?family=M+PLUS+Rounded+1c:wght@500;700;800&family=Noto+Sans+JP:wght@400;500;700&display=swap">
<style>
  :root {
    --coral: #e9866f;
    --coral-deep: #e07a62;
    --pink: #ef8097;
    --ink: #4a3f3b;
    --paper: #ffffff;
    --photo-light: #f6f1ec;
    --photo-mid: #e9ddd3;
    --photo-warm: #d9c3b3;
  }
  * { margin: 0; padding: 0; box-sizing: border-box; }
  html, body { width: 750px; height: 1200px; overflow: hidden; background: var(--paper); }
  .cover {
    position: relative;
    width: 750px; height: 1200px;
    background: var(--paper);
    font-family: "Noto Sans JP", sans-serif;
    color: var(--ink);
    overflow: hidden;
  }
  .cover-photo {
    position: absolute;
    left: 0; top: 500px; width: 750px; height: 700px;
    background:
      radial-gradient(ellipse 260px 220px at 470px 460px, var(--photo-warm), transparent 70%),
      radial-gradient(ellipse 200px 300px at 660px 280px, var(--photo-mid), transparent 75%),
      linear-gradient(180deg, var(--photo-light) 0%, #f1e8e0 60%, #e8dbd0 100%);
  }
  .endorsement {
    position: absolute;
    right: 0; top: 0;
    width: 112px; height: 190px;
    background: var(--coral);
    color: var(--paper);
    text-align: center;
    padding: 16px 4px 0;
  }
  .endorsement-lead { font-size: 13px; line-height: 1.45; font-weight: 500; letter-spacing: -0.5px; }
  .endorsement-name { font-size: 21px; line-height: 1.3; font-weight: 700; margin-top: 8px; }
  .title {
    position: absolute;
    left: 42px; top: 36px;
    font-family: "M PLUS Rounded 1c", sans-serif;
    color: var(--coral);
    font-weight: 800;
    line-height: 1;
  }
  .title-line { display: block; font-size: 130px; letter-spacing: 2px; }
  .title-line + .title-line { margin-top: 22px; }
  .title-sub {
    display: block;
    font-size: 62px;
    font-weight: 700;
    margin: 22px 0 0 178px;
    letter-spacing: 1px;
  }
  .author {
    position: absolute;
    left: 44px; top: 500px; right: 36px;
    display: flex; align-items: flex-end; justify-content: space-between;
  }
  .author-roles { font-size: 16px; line-height: 1.45; font-weight: 500; }
  .author-name { font-size: 27px; font-weight: 500; letter-spacing: 1px; }
  .author-name small { font-size: 19px; margin-left: 6px; }
  .catch {
    position: absolute;
    left: 44px; top: 556px;
    font-size: 46px; line-height: 1.42; font-weight: 500;
    color: var(--ink);
  }
  .catch em { font-style: normal; color: var(--coral-deep); }
  .gift {
    position: absolute;
    left: 30px; top: 1062px;
    width: 200px; height: 94px;
    background: var(--pink);
    color: var(--paper);
    border-radius: 8px;
    font-size: 22px; font-weight: 700; line-height: 1.35;
  }
  .gift svg { position: absolute; left: 14px; top: 16px; }
  .gift-text { position: absolute; left: 62px; top: 16px; }
  .bonus {
    position: absolute;
    left: 248px; top: 1074px;
    width: 478px; height: 76px;
    background: var(--coral);
    color: var(--paper);
    border-radius: 6px;
    padding: 6px 14px;
    font-size: 24px; font-weight: 700; line-height: 1.4;
    white-space: nowrap;
  }
</style>
</head>
<body>
<main class="cover">
  <div class="cover-photo" role="img" aria-label="妊婦のおなかに夫婦が手を添えている柔らかな写真"></div>

  <aside class="endorsement">
    <p class="endorsement-lead">胎内記憶の<br>世界的第一人者</p>
    <p class="endorsement-name">森下晃<br>先生推薦</p>
  </aside>

  <h1 class="title">
    <span class="title-line">お産が</span>
    <span class="title-line">軽くなる</span>
    <span class="title-sub">胎内記憶の物語</span>
  </h1>

  <div class="author">
    <p class="author-roles">全国育み言葉研究会認定講師<br>マタニティライフしあわせアドバイザー</p>
    <p class="author-name">北浦ミレーユ詩織<small>著</small></p>
  </div>

  <p class="catch"><em>夫婦</em>で学ぶ<br>おなかの<br>赤ちゃんとの<br>コミュニケーション</p>

  <div class="gift">
    <svg width="34" height="34" viewBox="0 0 34 34" fill="none" stroke="#ffffff" stroke-width="2.5" aria-hidden="true">
      <rect x="4" y="12" width="26" height="7"/>
      <rect x="6" y="19" width="22" height="12"/>
      <line x1="17" y1="12" x2="17" y2="31"/>
      <path d="M17 12 C12 4 6 7 10 12 M17 12 C22 4 28 7 24 12"/>
    </svg>
    <span class="gift-text">読者限定<br>プレゼント</span>
  </div>

  <p class="bonus">タイプ別おなかの赤ちゃんとの<br>コミュニケーションの始め方</p>
</main>
</body>
</html>
```